Civic Bastion Business Cards
Business Card for Civic Bastion
Project: Civic Bastion Business Cards
Civic Bastion Business Cards - Law
Creative Brief
Professional
Dorian Hale
Chairman/CEO
384 S. Wren Hollow Dr. Suite 212 Houston, TX 77031
dorian@civicbastion.example
www.civicbastion.example
I need another version for the following partner (all other information remains the same except the following): Russell T. Monday Chief Legal Officer email: russ@civicbastion.example
I am thinking a bigger version of the logo on the front to be used on the back of the card. Along with: To file a claim, please call toll free 1.888.555-0147

```html
<!DOCTYPE html>
<html lang="en">
<head>
<meta charset="utf-8">
<title>Civic Bastion Business Cards</title>
<link rel="stylesheet" href="https://fonts.googleapis.com/css2?family=Exo+2:wght@400;500;600&display=swap">
<style>
  :root {
    --backdrop: #e4e5e7;
    --card-white: #fbfbfb;
    --card-dark: #2a2a2b;
    --brand-blue: #2494c9;
    --brand-orange: #c4782f;
    --ink: #3a3a3a;
    --ink-soft: #6d6d6d;
    --ink-light: #c9c9c9;
  }
  * { box-sizing: border-box; margin: 0; padding: 0; }
  html, body { width: 1200px; height: 895px; overflow: hidden; }
  body {
    background: var(--backdrop);
    font-family: "Exo 2", sans-serif;
    display: flex;
    align-items: center;
    justify-content: center;
  }
  .card-set {
    display: grid;
    grid-template-columns: 540px 540px;
    grid-template-rows: 309px 309px;
    gap: 30px;
  }
  .card {
    position: relative;
    width: 540px;
    height: 309px;
    overflow: hidden;
    box-shadow: 0 6px 18px rgba(0,0,0,0.18);
  }
  /* front */
  .card-front { background: var(--card-white); }
  .brand {
    position: absolute;
    display: flex;
    align-items: center;
    gap: 10px;
  }
  .brand-front { left: 22px; top: 24px; }
  .brand-dot {
    width: 54px; height: 54px;
    border-radius: 50%;
    background: var(--brand-orange);
    flex: none;
  }
  .brand-name {
    font-weight: 500;
    color: var(--brand-blue);
    letter-spacing: 1px;
    font-size: 20px;
    line-height: 1;
  }
  .brand-tagline {
    font-size: 7px;
    color: var(--ink-soft);
    letter-spacing: 0.6px;
    margin-top: 4px;
  }
  .band-blue {
    position: absolute;
    left: 0; top: 122px;
    width: 206px; height: 44px;
    background: var(--brand-blue);
  }
  .band-orange {
    position: absolute;
    left: 206px; right: 0;
    top: 140px; height: 56px;
    background: var(--brand-orange);
    display: flex;
    align-items: center;
    padding-left: 20px;
    color: #fff;
    font-size: 13px;
    letter-spacing: 0.5px;
  }
  .person {
    position: absolute;
    right: 24px; top: 94px;
    width: 230px;
  }
  .person-name {
    font-size: 18px;
    font-weight: 500;
    color: var(--ink);
    letter-spacing: 1.5px;
    text-transform: uppercase;
    line-height: 1.2;
    white-space: nowrap;
  }
  .person-title {
    font-size: 11px;
    color: var(--ink);
    letter-spacing: 1px;
    text-transform: uppercase;
    white-space: nowrap;
  }
  .contact-list {
    position: absolute;
    list-style: none;
    display: flex;
    flex-direction: column;
    gap: 7px;
  }
  .contact-left { left: 22px; top: 204px; width: 180px; }
  .contact-right { left: 372px; top: 222px; }
  .contact-item {
    display: flex;
    align-items: flex-start;
    gap: 8px;
    font-size: 10px;
    line-height: 15px;
    color: var(--ink-soft);
  }
  .icon {
    width: 15px; height: 15px;
    background: var(--brand-orange);
    display: flex;
    align-items: center;
    justify-content: center;
    flex: none;
  }
  .icon svg { width: 9px; height: 9px; }
  .address { line-height: 13px; }
  /* back */
  .card-back {
    grid-column: 2;
    grid-row: 1 / span 2;
    align-self: center;
    background: var(--card-dark);
    display: flex;
    flex-direction: column;
    align-items: center;
    justify-content: center;
    gap: 22px;
  }
  .brand-back {
    position: static;
    flex-direction: column;
    gap: 10px;
    text-align: center;
  }
  .brand-back .brand-dot { width: 74px; height: 74px; }
  .brand-back .brand-name { font-size: 24px; }
  .claim-line {
    font-size: 11px;
    color: var(--ink-light);
    letter-spacing: 0.5px;
  }
</style>
</head>
<body>

<main class="card-set">

<section class="card card-front">
  <div class="brand brand-front">
    <span class="brand-dot"></span>
    <div>
      <p class="brand-name">CIVIC BASTION LLC</p>
      <p class="brand-tagline">Law and claims counsel</p>
    </div>
  </div>

  <div class="person">
    <p class="person-name">Dorian Hale</p>
    <p class="person-title">Chairman/CEO</p>
  </div>

  <div class="band-blue"></div>
  <div class="band-orange">www.civicbastion.example/123</div>

  <ul class="contact-list contact-left">
    <li class="contact-item">
      <span class="icon"><svg viewBox="0 0 10 10"><path d="M5 0.5a3.2 3.2 0 0 0-3.2 3.2C1.8 6 5 9.5 5 9.5s3.2-3.5 3.2-5.8A3.2 3.2 0 0 0 5 0.5zm0 4.4a1.2 1.2 0 1 1 0-2.4 1.2 1.2 0 0 1 0 2.4z" fill="#fff"/></svg></span>
      <span class="address">384 S. Wren Hollow Dr. Suite 212<br>Houston, TX 77031</span>
    </li>
    <li class="contact-item">
      <span class="icon"><svg viewBox="0 0 10 10"><path d="M2.2 0.8l1.6 1.8-0.9 1.3c0.6 1.3 1.5 2.2 2.9 2.9l1.3-0.9 1.8 1.6-1 1.5C4.4 8.6 1.4 5.6 0.8 1.8z" fill="#fff"/></svg></span>
      1.888.555-0147
    </li>
    <li class="contact-item">
      <span class="icon"><svg viewBox="0 0 10 10"><rect x="0.8" y="2" width="8.4" height="6" fill="none" stroke="#fff" stroke-width="1"/><path d="M0.8 2L5 5.4 9.2 2" fill="none" stroke="#fff" stroke-width="1"/></svg></span>
      dorian@civicbastion.example
    </li>
  </ul>

  <ul class="contact-list contact-right">
    <li class="contact-item"><span class="icon"></span>www.civicbastion.example</li>
    <li class="contact-item"><span class="icon"></span>www.chirpline.example</li>
    <li class="contact-item"><span class="icon"></span>www.facefold.example</li>
  </ul>
</section>

<section class="card card-back">
  <div class="brand brand-back">
    <span class="brand-dot"></span>
    <div>
      <p class="brand-name">CIVIC BASTION LLC</p>
      <p class="brand-tagline">Law and claims counsel</p>
    </div>
  </div>
  <p class="claim-line">To file a claim, please call toll free 1.888.555-0147</p>
</section>

<section class="card card-front">
  <div class="brand brand-front">
    <span class="brand-dot"></span>
    <div>
      <p class="brand-name">CIVIC BASTION LLC</p>
      <p class="brand-tagline">Law and claims counsel</p>
    </div>
  </div>

  <div class="person">
    <p class="person-name">Russell T. Monday</p>
    <p class="person-title">Chief Legal Officer</p>
  </div>

  <div class="band-blue"></div>
  <div class="band-orange">www.civicbastion.example/123</div>

  <ul class="contact-list contact-left">
    <li class="contact-item">
      <span class="icon"><svg viewBox="0 0 10 10"><path d="M5 0.5a3.2 3.2 0 0 0-3.2 3.2C1.8 6 5 9.5 5 9.5s3.2-3.5 3.2-5.8A3.2 3.2 0 0 0 5 0.5zm0 4.4a1.2 1.2 0 1 1 0-2.4 1.2 1.2 0 0 1 0 2.4z" fill="#fff"/></svg></span>
      <span class="address">384 S. Wren Hollow Dr. Suite 212<br>Houston, TX 77031</span>
    </li>
    <li class="contact-item">
      <span class="icon"><svg viewBox="0 0 10 10"><path d="M2.2 0.8l1.6 1.8-0.9 1.3c0.6 1.3 1.5 2.2 2.9 2.9l1.3-0.9 1.8 1.6-1 1.5C4.4 8.6 1.4 5.6 0.8 1.8z" fill="#fff"/></svg></span>
      1.888.555-0147
    </li>
    <li class="contact-item">
      <span class="icon"><svg viewBox="0 0 10 10"><rect x="0.8" y="2" width="8.4" height="6" fill="none" stroke="#fff" stroke-width="1"/><path d="M0.8 2L5 5.4 9.2 2" fill="none" stroke="#fff" stroke-width="1"/></svg></span>
      russ@civicbastion.example
    </li>
  </ul>

  <ul class="contact-list contact-right">
    <li class="contact-item"><span class="icon"></span>www.civicbastion.example</li>
    <li class="contact-item"><span class="icon"></span>www.chirpline.example</li>
    <li class="contact-item"><span class="icon"></span>www.facefold.example</li>
  </ul>
</section>

</main>

</body>
</html>
```